Corvana Wound Care Business card design

We need a business card designed around our logo which was provided. The logo of preference is the colored. Also the colors and fonts were provided.

Target Market(s)

Our Referral partners are home health agencies.

Industry/Entity Type

Healthcare

Contact Information for Business Card

Name , Phone #, Email , Title

Requirements
Nice to have
• Creativity
Should not have
• basic

```html
<!DOCTYPE html>
<html lang="en">
<head>
<meta charset="utf-8">
<title>Corvana Wound Care – Business Card</title>
<link rel="stylesheet" href="https://fonts.googleapis.com/css2?family=Montserrat:wght@400;600;700&family=Mulish:ital,wght@0,400;1,700&display=swap">
<style>
  :root {
    --stage: #03051c;
    --navy: #2a4795;
    --sky: #07a3e3;
    --mid-blue: #1188cc;
    --white: #ffffff;
  }
  * { margin: 0; padding: 0; box-sizing: border-box; }
  html, body { width: 1200px; height: 1200px; overflow: hidden; background: var(--stage); }
  .stage { position: relative; width: 1200px; height: 1200px; }

  .card { position: absolute; overflow: hidden; }
  .card-front { left: 240px; top: 180px; width: 680px; height: 389px; background: var(--white); }
  .card-back {
    left: 243px; top: 608px; width: 677px; height: 386px;
    background: linear-gradient(180deg, var(--mid-blue) 0%, var(--mid-blue) 35%, var(--navy) 72%, var(--navy) 100%);
  }

  .wave { position: absolute; left: 0; width: 680px; }
  .wave-top { top: 0; height: 60px; }
  .wave-bottom { bottom: 0; height: 52px; }

  .brand { position: absolute; display: flex; align-items: center; gap: 12px; }
  .brand-mark { width: 40px; height: 40px; border-radius: 8px; flex: 0 0 auto; }
  .brand-name { font-family: "Montserrat", sans-serif; font-weight: 700; white-space: nowrap; }
  .card-front .brand { left: 32px; top: 90px; }
  .card-front .brand-mark { background: var(--navy); }
  .card-front .brand-name { color: var(--navy); font-size: 22px; }
  .card-back .brand { left: 50%; top: 170px; transform: translateX(-50%); gap: 16px; }
  .card-back .brand-mark { width: 52px; height: 52px; border-radius: 10px; background: var(--white); }
  .card-back .brand-name { color: var(--white); font-size: 34px; }

  .tagline {
    position: absolute; left: 368px; top: 72px; width: 272px;
    font-family: "Mulish", sans-serif; font-style: italic; font-weight: 700;
    font-size: 16.5px; line-height: 21px; color: var(--navy); text-align: center;
  }

  .person { position: absolute; left: 40px; top: 208px; width: 320px; text-align: center; color: var(--navy); }
  .person-name { font-family: "Montserrat", sans-serif; font-weight: 700; font-size: 30px; letter-spacing: 0.5px; line-height: 36px; white-space: nowrap; }
  .person-title { font-family: "Montserrat", sans-serif; font-weight: 400; font-size: 14px; letter-spacing: 4.5px; margin-top: 2px; white-space: nowrap; }

  .contact-panel {
    position: absolute; left: 388px; top: 150px; width: 253px; height: 156px;
    border-radius: 22px;
    background: linear-gradient(180deg, var(--sky) 0%, #0c8fd6 40%, var(--navy) 100%);
    color: var(--white); font-family: "Mulish", sans-serif;
  }
  .contact-row { position: absolute; left: 16px; right: 10px; display: flex; align-items: center; gap: 16px; }
  .contact-row svg { width: 16px; height: 16px; flex: 0 0 16px; }
  .contact-text { font-size: 13.5px; line-height: 17px; white-space: nowrap; }
  .contact-text strong { font-family: "Montserrat", sans-serif; font-weight: 700; font-size: 15px; margin-left: 6px; }
  .row-area { top: 26px; }
  .row-area .contact-text { font-size: 13px; }
  .row-tel { top: 71px; }
  .row-fax { top: 95px; }
  .row-web { top: 122px; }
  .row-web .contact-text { font-size: 16px; }
</style>
</head>
<body>
<main class="stage">

  <section class="card card-front" aria-label="Business card front">
    <svg class="wave wave-top" viewBox="0 0 680 60" preserveAspectRatio="none">
      <defs>
        <linearGradient id="topBand" x1="0" x2="1" y1="0" y2="0">
          <stop offset="0" stop-color="#07a3e3"/>
          <stop offset="0.5" stop-color="#2a4795"/>
          <stop offset="1" stop-color="#2a4795"/>
        </linearGradient>
      </defs>
      <path d="M0 0 H680 V48 C620 24 540 14 461 15 C330 17 180 42 60 42 C30 42 12 41 0 39 Z" fill="url(#topBand)"/>
    </svg>

    <div class="brand">
      <span class="brand-mark"></span>
      <span class="brand-name">Corvana Wound Care</span>
    </div>

    <p class="tagline">Focused healing care so you can return to the life you love</p>

    <div class="person">
      <h1 class="person-name">DANIEL HAYES</h1>
      <p class="person-title">GENERAL SURGEON</p>
    </div>

    <div class="contact-panel">
      <div class="contact-row row-area">
        <svg viewBox="0 0 16 16"><path d="M8 1a5 5 0 0 0-5 5c0 3.6 5 9 5 9s5-5.4 5-9a5 5 0 0 0-5-5zm0 7a2 2 0 1 1 0-4 2 2 0 0 1 0 4z" fill="#fff"/></svg>
        <span class="contact-text">Serving the Greater Metro Area<br>&amp; Surrounding Counties</span>
      </div>
      <div class="contact-row row-tel">
        <svg viewBox="0 0 16 16"><path d="M3.5 1.5l2.3.4 1 3-1.6 1.2a8 8 0 0 0 4.7 4.7l1.2-1.6 3 1 .4 2.3c-.5 1.2-1.6 2-2.9 2C6.2 14.5 1.5 9.8 1.5 4.4c0-1.3.8-2.4 2-2.9z" fill="#fff"/></svg>
        <span class="contact-text">TEL :<strong>678-555-0142</strong></span>
      </div>
      <div class="contact-row row-fax">
        <svg viewBox="0 0 16 16"><rect x="4" y="1" width="8" height="4" fill="#fff"/><rect x="1" y="6" width="14" height="6" rx="1" fill="#fff"/><rect x="5" y="10" width="6" height="5" fill="#fff" stroke="#1a6cc0" stroke-width="1"/></svg>
        <span class="contact-text">FAX:<strong>678-555-0187</strong></span>
      </div>
      <div class="contact-row row-web">
        <svg viewBox="0 0 16 16" fill="none" stroke="#fff" stroke-width="1"><circle cx="8" cy="8" r="6.5"/><ellipse cx="8" cy="8" rx="3" ry="6.5"/><path d="M1.5 8h13M2.5 4.8h11M2.5 11.2h11"/></svg>
        <span class="contact-text">www.corvanacare.com</span>
      </div>
    </div>

    <svg class="wave wave-bottom" viewBox="0 0 680 52" preserveAspectRatio="none">
      <defs>
        <linearGradient id="bottomBand" x1="0" x2="1" y1="0" y2="0">
          <stop offset="0" stop-color="#2a4795"/>
          <stop offset="0.45" stop-color="#2158a6"/>
          <stop offset="1" stop-color="#07a3e3"/>
        </linearGradient>
      </defs>
      <path d="M0 7 C30 3 60 1 80 1 C200 1 330 27 461 27 C560 27 630 14 680 0 V52 H0 Z" fill="url(#bottomBand)"/>
    </svg>
  </section>

  <section class="card card-back" aria-label="Business card back">
    <div class="brand">
      <span class="brand-mark"></span>
      <span class="brand-name">Corvana Wound Care</span>
    </div>
  </section>

</main>
</body>
</html>
```